Travel Group 'Lydgate Group' needs a new business card design

Lydgate Group is a diverse business specialising in bespoke, tailor made holidays to suit all budgets and we are specialists in planning exciting day/short trips to suit all markets. Our target market is very varied going from the corporate client and as well as people in the community who simply want to experience something special.
We are looking for a card design that will encourage people to look at our websites and social media platforms and to see for themselves the different facets to our business. It is essential that the card has social media icons for Trellis, Murmur and Lumen. We are looking for a card with a blank background with no pictures and for the front side to have the attached Lydgate logo. The card should have similar colour scheme to the attached Lydgate logo.
The card must have the following information on one side:
Maud Penrose
Business Development Manager
maudpenrose@lydgatevoyages.example
Lydgate Group, 87 Quarry Lane
Harrowby, Westmarsh, Scotland KA19 4TN
+44 (0)1294 730182
And then the card must have the following on the second side:
(Lydgate logo)
(social media icons)
www.lydgatevoyages.example
www.lydgateoutings.example
Target Market(s)
Our target market is very varied going from the corporate client and as well as people in the community who simply want to experience something special.
Industry/Entity Type
Business
Contact Information for Business Card
Maud Penrose
+44 (0)1294 730182
(Lydgate logo)
(social media icons)
www.lydgatevoyages.example
www.lydgateoutings.example
Requirements
Must have
- It is essential that the card has social media icons for Trellis, Murmur & Lumen.
Should not have
- Should not have any images other than Lydgate logo.

```html
<!DOCTYPE html>
<html lang="en">
<head>
<meta charset="utf-8">
<title>Lydgate Group – Business Card</title>
<link rel="stylesheet" href="https://fonts.googleapis.com/css2?family=Open+Sans:wght@400;600;700&display=swap">
<style>
  :root{
    --stage:#e9e9e9;
    --navy:#2a2360;
    --purple:#5a3798;
    --ink:#4b2f8d;
    --pink:#e0218a;
    --paper:#ffffff;
  }
  *{box-sizing:border-box;margin:0;padding:0}
  html,body{width:1200px;height:900px;overflow:hidden;background:var(--stage)}
  body{font-family:"Open Sans",Verdana,sans-serif;position:relative}
  .card{
    position:absolute;top:160px;width:360px;height:580px;border-radius:16px;overflow:hidden;
    box-shadow:0 4px 0 #cfcfcf,0 8px 0 #bdbdbd,0 12px 24px rgba(0,0,0,.18);
  }
  .card--front{left:220px;background:var(--paper);padding:34px 30px 0 34px}
  .card--back{left:620px;background:var(--navy)}

  .holder-name{font-size:30px;font-weight:700;color:var(--purple);letter-spacing:.5px;line-height:1.1}
  .holder-role{font-size:14px;color:var(--pink);margin-top:4px}
  .contact-list{list-style:none;margin-top:26px}
  .contact-list li{display:flex;align-items:flex-start;gap:10px;font-size:13.5px;color:var(--ink);line-height:1.45;margin-bottom:2px}
  .contact-list li.gap{margin-top:12px}
  .contact-list svg{flex:none;width:14px;height:14px;margin-top:3px}
  .dot{flex:none;width:10px;height:10px;border-radius:50%;background:var(--pink);margin:5px 2px 0 2px}

  .wordmark{position:absolute;left:0;right:0;bottom:70px;text-align:center;
    font-size:44px;font-weight:700;letter-spacing:6px;color:var(--navy)}

  .back-disc{position:absolute;left:-20px;top:40px;width:430px;height:430px;border-radius:50%;
    background:radial-gradient(circle at 50% 50%,#ffffff 0 55%,#f3c6e0 72%,#c4307f 88%,#6a2a86 100%)}
  .back-wordmark{position:absolute;left:0;right:0;top:232px;text-align:center;
    font-size:40px;font-weight:700;letter-spacing:5px;color:var(--navy)}
  .social-row{position:absolute;left:0;right:0;bottom:40px;display:flex;justify-content:center;align-items:center;gap:16px}
  .social-row .rule{width:34px;height:2px;background:var(--pink)}
  .social{display:flex;align-items:center;gap:6px;font-size:12px;color:var(--paper)}
  .social::before{content:"";width:16px;height:16px;border-radius:50%;background:var(--paper)}
</style>
</head>
<body>

<section class="card card--front">
  <h1 class="holder-name">Maud Penrose</h1>
  <p class="holder-role">Business Development Manager</p>
  <ul class="contact-list">
    <li><svg viewBox="0 0 16 16"><circle cx="8" cy="8" r="7" fill="none" stroke="#e0218a" stroke-width="1.5"/><path d="M5.5 4.5l1.5 0 .7 1.8-1 .8a5 5 0 0 0 2.2 2.2l.8-1 1.8.7v1.5c-3.5 0-6-2.5-6-6z" fill="#e0218a"/></svg>+44 (0)1632 730182</li>
    <li><svg viewBox="0 0 16 16"><rect x="1" y="3" width="14" height="10" fill="#e0218a"/><path d="M1 3l7 6 7-6" fill="none" stroke="#fff" stroke-width="1.3"/></svg>maudpenrose@lydgatevoyages.example</li>
    <li class="gap"><svg viewBox="0 0 16 16"><circle cx="8" cy="8" r="7" fill="#e0218a"/><path d="M1 8h14M8 1c-3 3-3 11 0 14M8 1c3 3 3 11 0 14" fill="none" stroke="#fff" stroke-width="1"/></svg>www.lydgatevoyages.example</li>
    <li><svg viewBox="0 0 16 16"><circle cx="8" cy="8" r="7" fill="#e0218a"/><path d="M1 8h14M8 1c-3 3-3 11 0 14M8 1c3 3 3 11 0 14" fill="none" stroke="#fff" stroke-width="1"/></svg>www.lydgateoutings.example</li>
    <li class="gap"><svg viewBox="0 0 16 16"><path d="M8 15s5-5.5 5-9A5 5 0 0 0 3 6c0 3.5 5 9 5 9z" fill="#e0218a"/><circle cx="8" cy="6" r="2" fill="#fff"/></svg>Lydgate Group, 87 Quarry Lane<br>Harrowby, Westmarsh, Scotland KA19 4TN</li>
    <li class="gap"><span class="dot"></span>www.murmur.example/lydgatevoyages</li>
    <li><span class="dot"></span>www.trellis.example/lydgateoutings</li>
    <li><span class="dot"></span>www.lumen.example/lydgatevoyages</li>
  </ul>
  <p class="wordmark">LYDGATE</p>
</section>

<section class="card card--back">
  <div class="back-disc" role="img" aria-label="Sweeping pink and navy ribbon decoration"></div>
  <p class="back-wordmark">LYDGATE</p>
  <div class="social-row">
    <span class="rule"></span>
    <span class="social">Trellis</span>
    <span class="social">Murmur</span>
    <span class="social">Lumen</span>
    <span class="rule"></span>
  </div>
</section>

</body>
</html>
```